Business card and stationary designs for Harbor Summit Mentor
Harbor Summit Mentor
Business card and stationary designs for Harbor Summit Mentor - Consulting
Creative Brief
Professional
Reed Calloway
Executive & Professional Coach
4187 Willow Bend Lane Dallas TX 75231
RCalloway@harborsummitmentor.example
www.HarborSummitMentor.example
I want this to look clean, cutting edge, and for the design to stand out.
On the back of the business card I would like my logo and the phrase "Executive & Professional Coaching"

```html
<!DOCTYPE html>
<html lang="en">
<head>
<meta charset="utf-8">
<title>Harbor Summit Mentor – Business Card</title>
<link href="https://fonts.googleapis.com/css2?family=Open+Sans:wght@400;600;700&display=swap" rel="stylesheet">
<style>
  :root {
    --page-bg: #d9d6d2;
    --card-bg: #eceeef;
    --card-edge: #c9cccf;
    --ink-dark: #2b2d30;
    --ink-mid: #4a4d52;
    --rule: #5a5d62;
    --band: #7b7e83;
    --band-tab: #3a3c40;
    --band-text: #f4f4f4;
  }
  * { margin: 0; padding: 0; box-sizing: border-box; }
  html, body {
    width: 1200px; height: 768px; overflow: hidden;
    background: var(--page-bg);
    font-family: "Open Sans", Arial, sans-serif;
  }
  .stage { position: relative; width: 1200px; height: 768px; }
  .card {
    position: absolute; left: 100px; top: 98px;
    width: 1000px; height: 572px;
    background: var(--card-bg);
    border: 1px solid var(--card-edge);
    border-radius: 10px;
    overflow: hidden;
    box-shadow: 0 18px 40px rgba(0,0,0,0.18);
  }
  .brand {
    position: absolute; left: 600px; top: 120px; width: 330px;
    text-align: center;
    color: var(--ink-dark);
    font-weight: 600; font-size: 30px; letter-spacing: 2px;
    line-height: 1.25; text-transform: uppercase;
  }
  .holder { position: absolute; left: 78px; top: 238px; color: var(--ink-dark); }
  .holder-name { font-size: 46px; font-weight: 700; letter-spacing: 0.5px; }
  .holder-title { margin-top: 38px; font-size: 34px; color: var(--ink-mid); }
  .name-rule { position: absolute; left: 70px; top: 290px; }
  .contact {
    position: absolute; right: 72px; top: 318px;
    text-align: right; color: var(--ink-mid);
    font-size: 22px; line-height: 1.45;
  }
  .contact .address { margin-bottom: 24px; }
  .contact-line { display: flex; justify-content: flex-end; align-items: center; gap: 10px; }
  .contact-line svg { width: 18px; height: 18px; fill: var(--ink-mid); }
  .footer-band { position: absolute; left: 0; bottom: 0; width: 1000px; height: 70px; }
  .footer-web {
    position: absolute; left: 48px; bottom: 18px;
    color: var(--band-text); font-size: 20px; letter-spacing: 0.3px;
  }
</style>
</head>
<body>
<div class="stage">
  <div class="card">
    <div class="brand">Harbor Summit<br>Mentor</div>

    <div class="holder">
      <div class="holder-name">Owen T Marsh</div>
      <div class="holder-title">CEO</div>
    </div>

    <svg class="name-rule" width="880" height="12" viewBox="0 0 880 12">
      <path d="M0 6 H380 L392 2 H880" fill="none" stroke="var(--rule)" stroke-width="2"/>
    </svg>

    <div class="contact">
      <div class="address">214.9th floor,Plaza<br>Crestview Road NTH</div>
      <div class="contact-line">014 552 7380
        <svg viewBox="0 0 24 24"><path d="M6.6 10.8a15.1 15.1 0 0 0 6.6 6.6l2.2-2.2c.3-.3.7-.4 1-.2 1.1.4 2.3.6 3.6.6.6 0 1 .4 1 1V20c0 .6-.4 1-1 1C10.6 21 3 13.4 3 4c0-.6.4-1 1-1h3.5c.6 0 1 .4 1 1 0 1.3.2 2.5.6 3.6.1.3 0 .7-.2 1z"/></svg>
      </div>
      <div class="contact-line">owen@mailbox.example
        <svg viewBox="0 0 24 24"><path d="M3 5h18v14H3z M4 6.5v.6l8 5.4 8-5.4v-.6z" fill-rule="evenodd"/></svg>
      </div>
      <div class="contact-line">www.harborsummitmentor.example
        <svg viewBox="0 0 24 24"><circle cx="12" cy="12" r="9" fill="none" stroke="var(--ink-mid)" stroke-width="2"/><path d="M3 12h18M12 3c3 3 3 15 0 18M12 3c-3 3-3 15 0 18" fill="none" stroke="var(--ink-mid)" stroke-width="1.5"/></svg>
      </div>
    </div>

    <svg class="footer-band" viewBox="0 0 1000 70" preserveAspectRatio="none">
      <rect x="0" y="36" width="1000" height="34" fill="var(--band)"/>
      <path d="M0 10 H300 C325 10 330 36 355 36 V70 H0 Z" fill="var(--band-tab)"/>
    </svg>
    <div class="footer-web">www.harborsummitmentor.example</div>
  </div>
</div>
</body>
</html>
```